Recrutering company needs a Roll-Up Design

We need a Roll-Up Design for our company, which is dedicated to personnel selection. We would like the roll-up to feature our logo and the silhouette of the buildings shown in one of the uploaded photos (the one called "BelorquiFestuOre7"). Additionally, we'd like to incorporate the words "Persones," "Talent," and "Èxit" with shadows using the English equivalents instead of the original ones, so: "People" for "Persones," "Talent" for "Talent," and "Success" for "Èxit."

The color of the logo can be changed to red, and the overall design can incorporate this color. As the design is for a roll-up, its essential to take into account a 4cm margin.

```html
<!DOCTYPE html>
<html lang="en">
<head>
<meta charset="utf-8">
<title>Belorqui Roll-Up</title>
<link rel="stylesheet" href="https://fonts.googleapis.com/css2?family=Cinzel:wght@400;700&family=Marcellus&family=Montserrat:wght@500&display=swap">
<style>
  :root {
    --backdrop: #b9aeae;
    --paper: #f7f7f7;
    --wave-edge: #b3b3b3;
    --wine-top: #a53f60;
    --wine-bottom: #5a1217;
    --brand-ink: #55545a;
    --brand-red: #c23b62;
    --word-ink: #ffffff;
    --word-shadow: #2a0a0e;
    --town-light: #e05a7f;
    --town-dark: #b8324f;
    --snow: #f3c3d1;
  }
  * { margin: 0; padding: 0; box-sizing: border-box; }
  html, body {
    width: 1200px;
    height: 1200px;
    overflow: hidden;
    background: var(--backdrop);
  }
  .canvas {
    position: relative;
    width: 1200px;
    height: 1200px;
  }
  .rollup {
    position: absolute;
    left: 370px;
    top: 25px;
    width: 460px;
    height: 1150px;
    background: linear-gradient(180deg, var(--wine-top) 40%, var(--wine-bottom) 88%);
    overflow: hidden;
    box-shadow: 0 6px 18px rgba(0,0,0,0.18);
  }
  .rollup__wave {
    position: absolute;
    left: 0;
    top: 0;
    width: 460px;
    height: 520px;
  }
  .brand {
    position: absolute;
    left: 0;
    top: 215px;
    width: 100%;
    text-align: center;
  }
  .brand__mark {
    display: inline-block;
    width: 44px;
    height: 44px;
    border-radius: 50%;
    background: var(--brand-red);
    margin-bottom: 18px;
  }
  .brand__name {
    font-family: "Marcellus", serif;
    font-size: 46px;
    letter-spacing: 5px;
    color: var(--brand-ink);
    line-height: 1;
  }
  .brand__tagline {
    margin-top: 8px;
    font-family: "Montserrat", sans-serif;
    font-weight: 500;
    font-size: 13px;
    letter-spacing: 4px;
    color: var(--brand-red);
  }
  .values {
    position: absolute;
    left: 0;
    top: 545px;
    width: 100%;
    list-style: none;
    text-align: center;
  }
  .values__word {
    font-family: "Cinzel", serif;
    font-weight: 400;
    font-size: 52px;
    color: var(--word-ink);
    letter-spacing: 2px;
    line-height: 1;
    height: 112px;
    text-shadow: 3px 3px 2px var(--word-shadow);
  }
  .townscape {
    position: absolute;
    left: 0;
    bottom: 0;
    width: 460px;
    height: 260px;
  }
</style>
</head>
<body>
<main class="canvas">
  <section class="rollup">
    <svg class="rollup__wave" viewBox="0 0 460 520" aria-hidden="true">
      <path d="M0 0 H460 V215 C470 330 420 500 270 500 C180 500 120 430 0 455 Z" fill="var(--wave-edge)"/>
      <path d="M0 0 H460 V200 C465 320 410 488 270 488 C180 488 120 420 0 445 Z" fill="var(--paper)"/>
    </svg>

    <header class="brand">
      <span class="brand__mark"></span>
      <h1 class="brand__name">BELORQUI</h1>
      <p class="brand__tagline">SELECCIÓ DE TALENT</p>
    </header>

    <ul class="values">
      <li class="values__word">PEOPLE</li>
      <li class="values__word">TALENT</li>
      <li class="values__word">SUCCESS</li>
    </ul>

    <svg class="townscape" viewBox="0 0 460 260" role="img" aria-label="Illustrated silhouette of an old factory town: brick buildings with lit windows, a tall chimney and small houses on pink snowy ground">
      <defs>
        <linearGradient id="town-fill" x1="0" y1="0" x2="0" y2="1">
          <stop offset="0" stop-color="var(--town-dark)" stop-opacity="0"/>
          <stop offset="0.35" stop-color="var(--town-dark)"/>
          <stop offset="0.75" stop-color="var(--town-light)"/>
          <stop offset="1" stop-color="var(--snow)"/>
        </linearGradient>
      </defs>
      <rect x="0" y="0" width="460" height="260" fill="url(#town-fill)"/>
    </svg>
  </section>
</main>
</body>
</html>
```